T.R.K Nearby porch digetal offers systems

On the front side of the door hanger with the 14 coupons . It show the customers how their ad will look on the door hanger. On the second side it sells and tells the customer about the benefits about why they should advertise with us an be on the door hanger coupon.. hope this help.

this a mock door hanger advertisement for customer to see before purchasing ad space on the door hanger..

Coupon are just example for the customers to see. Make coupon 25% off to 80% off coupons on both sides

Target Market(s)

white men age 25 to 60 years of age income $50.00 to $250.00 a year

Industry/Entity Type

adversitiseing AGENCY

Font styles to use
Sans Serif

Colors
FFF300
FFF600
FEFA6F
FFFEC7
FFFEE8
FFC000
F8CF3A
FAE287
FDF2CF
FEFAEE
F0912C
F2A743
F7CA91
FBE8D2
FDF5EE
EE7325
F08F49
F5BC92
FAE3D3
FDF4ED

Requirements
Must have
• image of product MADE UP PHONE NUMBER 412 AREA discout AMOUT 25% UP TO 80 % and Q.R CODE
Nice to have
• image , make up phone number area code 412 DISCOUNT 25 % ON UP TO 80%
Should not have
• phone number on coupon and Q.R CODE AND GRAFFIC OF PRODUCT OR SERVICE

```html
<!DOCTYPE html>
<html lang="en">
<head>
<meta charset="utf-8">
<title>Nearby Porch Offers System – Reach 10,000 Homes</title>
<link rel="stylesheet" href="https://fonts.googleapis.com/css2?family=Montserrat:wght@600;700;800;900&display=swap">
<style>
  :root{
    --red-deep:#c8141b;
    --red:#e2231a;
    --orange-red:#ee4a1f;
    --orange:#f07a22;
    --amber:#ffa51e;
    --yellow:#fff300;
    --white:#ffffff;
    --sky-top:#e8a45a;
    --sky-mid:#d9773a;
    --roof:#7a4636;
    --shadow:rgba(60,0,0,.35);
  }
  *{margin:0;padding:0;box-sizing:border-box;}
  html,body{width:1200px;height:3596px;overflow:hidden;}
  body{font-family:"Montserrat",Arial,sans-serif;color:var(--white);}
  .banner{
    position:relative;width:1200px;height:3596px;overflow:hidden;
    background:linear-gradient(180deg,var(--orange) 0%,var(--orange) 30%,var(--orange-red) 55%,var(--red) 78%,var(--red-deep) 100%);
  }
  .neighborhood-photo{
    position:absolute;left:0;top:0;width:1200px;height:1150px;
    background:linear-gradient(180deg,var(--sky-top) 0%,var(--sky-mid) 28%,var(--roof) 48%,#a8542c 66%,rgba(240,122,34,0) 100%);
  }
  .neighborhood-photo::after{
    content:"";position:absolute;inset:0;
    background:radial-gradient(ellipse 60% 30% at 55% 48%,rgba(255,220,160,.35),rgba(255,220,160,0) 70%);
  }

  /* Brand lockup */
  .brand{position:absolute;left:230px;top:64px;width:740px;height:230px;}
  .brand-pill{
    position:absolute;left:90px;top:38px;width:650px;height:160px;
    background:var(--red);border:6px solid var(--white);border-radius:80px;
  }
  .brand-dot{
    position:absolute;left:0;top:0;width:230px;height:230px;border-radius:50%;
    background:var(--white);border:10px solid var(--red);
  }
  .brand-name{
    position:absolute;left:262px;top:60px;width:460px;
    font-weight:800;font-size:44px;line-height:1.05;text-transform:uppercase;color:var(--white);
  }

  .headline{
    position:absolute;left:112px;top:712px;
    font-weight:900;font-size:176px;line-height:.93;letter-spacing:8px;text-transform:uppercase;
    text-shadow:0 6px 14px var(--shadow);
  }

  .promise{position:absolute;top:1300px;display:flex;align-items:center;justify-content:center;
    flex-direction:column;height:182px;background:var(--red);border:6px solid var(--white);border-radius:26px;
    text-transform:uppercase;line-height:1;}
  .promise-no{font-weight:900;font-size:92px;}
  .promise-label{font-weight:800;font-size:40px;margin-top:8px;}
  .promise--contract{left:108px;width:300px;}
  .promise--commitment{left:440px;width:386px;}

  .services{position:absolute;left:100px;top:1535px;list-style:none;}
  .services li{display:flex;align-items:center;gap:26px;font-weight:800;font-size:90px;line-height:1.13;
    text-transform:uppercase;text-shadow:0 4px 10px var(--shadow);}
  .services svg{width:64px;height:64px;flex:none;}

  .fee-tag{position:absolute;left:100px;top:1900px;background:var(--yellow);color:var(--red-deep);
    font-weight:800;font-size:36px;padding:6px 16px;text-transform:uppercase;}
  .benefits{position:absolute;left:100px;top:1972px;list-style:none;}
  .benefits li{display:flex;align-items:center;gap:16px;font-weight:700;font-size:33px;line-height:52px;text-transform:uppercase;}
  .benefits svg{width:36px;height:36px;flex:none;}

  .door-hanger{position:absolute;left:850px;top:640px;width:230px;height:1180px;}

  .campaign{
    position:absolute;left:88px;top:2290px;width:944px;height:822px;
    background:linear-gradient(135deg,var(--amber) 0%,var(--orange) 55%,var(--orange-red) 100%);
    box-shadow:0 10px 30px var(--shadow);
  }
  .campaign-text{position:absolute;left:44px;top:56px;font-weight:900;text-transform:uppercase;line-height:.95;
    text-shadow:0 5px 12px var(--shadow);}
  .campaign-small{font-size:74px;display:block;}
  .campaign-big{font-size:176px;display:block;letter-spacing:-2px;}
  .campaign-small.last{margin-top:14px;}
  .campaign-hanger{position:absolute;right:8px;top:16px;width:164px;height:790px;
    background:linear-gradient(180deg,#f2e9dc 0%,#d84a2a 18%,#3a62b4 40%,#f3efe8 55%,#e3a02a 72%,#c02a22 88%,#f2e9dc 100%);}

  .call-line{position:absolute;left:0;width:1200px;top:3282px;text-align:center;font-weight:800;font-size:50px;text-transform:uppercase;}
  .phone{position:absolute;left:0;width:1200px;top:3370px;text-align:center;font-weight:800;font-size:110px;letter-spacing:1px;}
</style>
</head>
<body>
<main class="banner">
  <div class="neighborhood-photo" role="img" aria-label="Aerial view of a suburban neighborhood with houses around a roundabout at sunset"></div>

  <div class="brand">
    <div class="brand-pill"></div>
    <div class="brand-dot"></div>
    <div class="brand-name">Nearby Porch Offers System</div>
  </div>

  <h1 class="headline">Reach<br>10,000<br>Homes</h1>

  <div class="promise promise--contract"><span class="promise-no">No</span><span class="promise-label">Contract</span></div>
  <div class="promise promise--commitment"><span class="promise-no">No</span><span class="promise-label">Commitment</span></div>

  <ul class="services">
    <li><svg viewBox="0 0 24 24" fill="none" stroke="#fff" stroke-width="2"><rect x="2" y="4" width="20" height="13" rx="1"/><path d="M8 21h8M12 17v4"/></svg>We Design,</li>
    <li><svg viewBox="0 0 24 24" fill="none" stroke="#fff" stroke-width="2"><rect x="6" y="2" width="12" height="6"/><rect x="2" y="8" width="20" height="9" rx="1"/><rect x="6" y="14" width="12" height="8"/></svg>Print &amp;</li>
    <li><svg viewBox="0 0 24 24" fill="none" stroke="#fff" stroke-width="2"><path d="M3 10v4h4l8 5V5L7 10H3z"/><path d="M18 9c1.5 1.5 1.5 4.5 0 6"/></svg>Distribute</li>
  </ul>

  <div class="fee-tag">For an all-inclusive fee</div>
  <ul class="benefits">
    <li><svg viewBox="0 0 24 24" fill="none" stroke="#fff" stroke-width="2.4"><circle cx="12" cy="12" r="10"/><path d="M7 12l3.5 3.5L17 9"/></svg>10,000 local homes &amp; businesses combined</li>
    <li><svg viewBox="0 0 24 24" fill="none" stroke="#fff" stroke-width="2.4"><circle cx="12" cy="12" r="10"/><path d="M7 12l3.5 3.5L17 9"/></svg>Within 2-3 miles from your location</li>
    <li><svg viewBox="0 0 24 24" fill="none" stroke="#fff" stroke-width="2.4"><circle cx="12" cy="12" r="10"/><path d="M7 12l3.5 3.5L17 9"/></svg>All non-competing businesses</li>
    <li><svg viewBox="0 0 24 24" fill="none" stroke="#fff" stroke-width="2.4"><circle cx="12" cy="12" r="10"/><path d="M7 12l3.5 3.5L17 9"/></svg>A way to drive more locals to your business!</li>
  </ul>

  <svg class="door-hanger" viewBox="0 0 230 1180" preserveAspectRatio="none" role="img" aria-label="Sample door hanger printed with a column of colorful local business coupons">
    <defs>
      <linearGradient id="hangerFill" x1="0" y1="0" x2="0" y2="1">
        <stop offset="0" stop-color="#f3efe8"/>
        <stop offset=".15" stop-color="#d8402a"/>
        <stop offset=".32" stop-color="#4a6fc0"/>
        <stop offset=".48" stop-color="#f1ede6"/>
        <stop offset=".62" stop-color="#3d9ad2"/>
        <stop offset=".78" stop-color="#e6a22a"/>
        <stop offset=".92" stop-color="#c22a22"/>
        <stop offset="1" stop-color="#f3efe8"/>
      </linearGradient>
    </defs>
    <polygon points="70,0 226,30 216,1176 4,1150" fill="url(#hangerFill)"/>
  </svg>

  <section class="campaign">
    <p class="campaign-text">
      <span class="campaign-small">Only a</span>
      <span class="campaign-big">Few<br>Spots<br>Left</span>
      <span class="campaign-small last">In our spring<br>campaign!</span>
    </p>
    <div class="campaign-hanger" role="img" aria-label="Sample door hanger with example coupons"></div>
  </section>

  <p class="call-line">Call before your competition</p>
  <p class="phone">412-555-0187</p>
</main>
</body>
</html>
```